House Cleaning Website - Maid Services

Logo, landing page design with contact form - coded MUST BE MOBILE FRIENDLY

Cleaning business - maid service - i've added a few example websites

Clean, Smart Website Design that is built for getting leads

CONTENT FOR HOME PAGE -

Cleaning Seminole County Homes For Over 12 Years

Rosetta Cleans

* Trusted by your neighbors for more than a decade
* Affordable and flexible to accommodate your needs
* 200% Money Back Guarantee
* Up to 20% Discount on Continued Cleanings
* Same Day Cleanings

My Clients Are Happy
"Rosetta has been cleaning my home for the past 3 1/2 years and I couldn't be happier with her. I trust her with cleaning my home while I'm out of town and recommend her to my friends."

Target Market(s)

people looking for house cleaning

Industry/Entity Type

Cleaning Service

Contact Information for Business Card

Rosetta Cleans -
#321-555-0187
200% Guarantee
on back of card - $25 Referral Fee

Logo Text

Rosetta Cleans

Coding

Coded - Design and coding required

Number of Pages Required

3 page

Requirements
Must have
• 4 links in top toolbar - services, contact, free estimate and about
• *contact will be a popup form to contact
• *services will be a graphic similar to the one on this page ... https://www.brightbroomcrew.com/maid-services/
• *free estimate link will be a page with same questions as
• Must have landing page concept - I will be advertising to get people to submit their information...
• 1. Must have a "Request FREE Estimate" button that pops up a box for them to submit their information - name, number, email. Once they submit this information, they will be taken to a 2nd form to complete their details - If they dont complete the 2nd part I still receive the 1st part to call. The 2nd part will have same questions ashttps://www.tidyhenwick.com/local-house-cleaning/fl/west-miami/request-a-cleaning.aspx?cpgnId=FE0CA3B4-3A4C-4D9C-9B11-E69492B42092&scid=3554195&cid=2303288&tc=17072613580054989&rl_key=a0563857ec931d2a952e39d66a08939d&kw=77903:7716&pub_cr_id=200261568213&dynamic_proxy=1&primary_serv=www.tidyhenwick.com&rl_track_landing_pages=1
• 2. Must have pricing like https://www.brightbroomcrew.com/ 1 bedroom through 6 bedroom pricing base pricing graphic.
• 2.Must have a 200% satisfaction guarantee graphic
• 3.Must have phone number visible
• 4. graphics offering - 1st deep clean $25 Off - 10% Off Bi Weekly Cleanings - 20% Off Weekly Cleanings
• I like the clean look of this website https://www.pearlofsuds.com/ BUT want a more compact website like https://www.brightbroomcrew.com/
• Popup for when the try and x out saying Book Now And Receive $20 Off 1st Cleaning

```html
<!DOCTYPE html>
<html lang="en">
<head>
<meta charset="utf-8">
<title>Rosetta Cleans – Maid Services</title>
<link href="https://fonts.googleapis.com/css2?family=Open+Sans:ital,wght@0,400;0,600;0,700;1,400&display=swap" rel="stylesheet">
<style>
:root{
  --teal:#4fd0bf;
  --teal-light:#62d8c8;
  --teal-dark:#27ad9b;
  --coral:#f27772;
  --ink:#4a4f55;
  --muted:#8a9096;
  --footer:#222629;
  --footer-bar:#191c1e;
  --white:#ffffff;
  --soft:#f4f8f9;
}
*{box-sizing:border-box;margin:0;padding:0}
html,body{width:1200px;height:2260px;overflow:hidden}
body{font-family:"Open Sans",Arial,sans-serif;color:var(--ink);background:var(--white);position:relative}

/* header */
.site-header{position:absolute;top:0;left:0;width:1200px;height:60px;background:var(--white);box-shadow:0 1px 4px rgba(0,0,0,.08);z-index:5}
.brand{position:absolute;left:28px;top:16px;font-size:22px;font-weight:600;color:var(--ink);display:flex;align-items:center;gap:10px;line-height:28px}
.brand-mark{width:12px;height:12px;background:var(--ink)}
.header-contact{position:absolute;right:120px;top:4px;font-size:10px;color:var(--muted);line-height:13px}
.main-nav{position:absolute;right:36px;top:34px;display:flex;gap:8px;font-size:12px;font-weight:600}
.main-nav a{color:var(--ink);text-decoration:none;padding:2px 8px}
.main-nav a.active{border:1px solid var(--ink);border-radius:3px}

/* hero */
.hero{position:absolute;top:60px;left:0;width:1200px;height:390px}
.hero-photo{position:absolute;inset:0;background:linear-gradient(90deg,#cfe0e8 0%,#e9f1f4 35%,#f5f8f9 60%,#e4eef1 100%)}
.hero-badge{position:absolute;left:410px;top:140px;width:200px;height:200px;border-radius:50%;background:rgba(79,208,191,.35);display:flex;align-items:center;justify-content:center}
.hero-badge-inner{width:172px;height:172px;border-radius:50%;background:var(--teal);color:var(--white);text-align:center;padding-top:38px}
.hero-badge-inner .name{font-size:20px;font-weight:700}
.hero-badge-inner .tag{font-size:11px;margin-top:2px}
.hero-badge-inner .call{font-size:14px;font-weight:700;margin-top:12px}
.hero-badge-inner .phone{font-size:12px}

.contact-card{position:absolute;left:788px;top:50px;width:292px;height:320px;background:var(--teal);border-radius:4px;box-shadow:0 4px 14px rgba(0,0,0,.15);padding:0 26px;z-index:2}
.contact-card h2{margin:0 -26px;background:var(--coral);color:var(--white);text-align:center;font-size:20px;font-weight:600;height:46px;line-height:46px;border-radius:4px 4px 0 0}
.contact-card p{font-size:10px;color:var(--white);text-align:center;margin:10px 0 12px;line-height:14px}
.field{height:30px;background:var(--white);border-radius:2px;margin-bottom:11px;font-size:10px;color:var(--muted);padding:0 10px;line-height:30px}
.btn{display:inline-block;background:var(--coral);color:var(--white);font-weight:600;border-radius:3px;text-align:center}
.contact-card .btn{display:block;margin:4px auto 0;width:110px;height:32px;line-height:32px;font-size:13px}

.zigzag{position:absolute;left:0;width:1200px;height:12px;z-index:4}

/* about */
.about{position:absolute;top:450px;left:0;width:1200px;height:380px;background:var(--teal);z-index:2}
.section-title{font-size:30px;font-weight:600;text-align:center}
.title-rule{width:60px;height:3px;margin:8px auto 0;background:currentColor;opacity:.7}
.about .section-title{color:var(--white);position:absolute;top:30px;width:100%}
.about-text{position:absolute;left:120px;top:120px;width:500px;font-size:12px;line-height:20px;color:var(--white)}
.about .btn{position:absolute;left:120px;top:260px;width:110px;height:36px;line-height:36px;font-size:13px}
.about-photo{position:absolute;left:690px;top:110px;width:390px;height:150px;background:linear-gradient(180deg,#ffffff,#e5eef0)}

/* services */
.services{position:absolute;top:830px;left:0;width:1200px;height:560px;background:linear-gradient(180deg,#fff,var(--soft))}
.services .section-title{color:var(--teal);position:absolute;top:62px;width:100%}
.service{position:absolute;width:290px;display:flex;gap:14px}
.service-icon{flex:0 0 46px;height:46px;border-radius:6px;background:var(--teal);display:flex;align-items:center;justify-content:center}
.service h3{font-size:14px;font-weight:600;color:var(--ink);margin-bottom:4px}
.service p{font-size:10px;line-height:14px;color:var(--muted)}
.services-photo{position:absolute;left:430px;top:150px;width:340px;height:330px;background:radial-gradient(ellipse at 50% 45%,#f6d9d8 0%,#f8eeee 45%,rgba(255,255,255,0) 72%)}
.services-base{position:absolute;left:460px;top:486px;width:280px;height:6px;border-radius:3px;background:var(--teal)}

/* offers */
.offers{position:absolute;top:1390px;left:0;width:1200px;height:320px;background:var(--teal-light);z-index:2}
.offers .section-title{color:var(--white);position:absolute;top:36px;width:100%}
.offer{position:absolute;top:110px;width:240px;text-align:center;color:var(--white)}
.offer-ring{width:160px;height:160px;margin:0 auto;border-radius:50%;border:6px solid rgba(255,255,255,.35);padding:8px}
.offer-disc{width:100%;height:100%;border-radius:50%;background:var(--teal-dark);display:flex;flex-direction:column;align-items:center;justify-content:center}
.offer-disc .lead{font-size:12px;font-weight:600}
.offer-disc .value{font-size:30px;font-weight:700;line-height:38px}
.offer-disc .value small{font-size:13px;font-weight:600}
.offer-caption{margin-top:18px;font-size:13px;font-weight:600}

/* testimonials */
.clients{position:absolute;top:1710px;left:0;width:1200px;height:260px;background:var(--white)}
.clients .section-title{color:var(--teal);position:absolute;top:56px;width:100%}
.quote-mark{position:absolute;left:582px;top:126px;width:36px;height:36px}
.quote-text{position:absolute;left:320px;top:180px;width:560px;text-align:center;font-size:11px;line-height:17px;color:var(--muted);font-style:italic}
.dots{position:absolute;left:0;top:232px;width:100%;display:flex;justify-content:center;gap:8px}
.dots span{width:8px;height:8px;border-radius:50%;background:#d3dadd}
.dots span.on{background:var(--teal)}

/* newsletter */
.newsletter{position:absolute;top:1970px;left:0;width:1200px;height:60px;background:var(--teal)}
.newsletter h2{position:absolute;left:170px;top:14px;font-size:24px;font-weight:600;color:var(--white);line-height:32px}
.newsletter .field{position:absolute;left:470px;top:14px;width:320px;height:32px;margin:0;line-height:32px}
.newsletter .btn{position:absolute;left:800px;top:14px;width:120px;height:32px;line-height:32px;font-size:13px}

/* footer */
.site-footer{position:absolute;top:2030px;left:0;width:1200px;height:190px;background:var(--footer);color:#b9bec2}
.footer-col{position:absolute;top:30px;font-size:11px;line-height:24px}
.footer-col li{list-style:none}
.footer-col li::before{content:"› ";color:var(--teal)}
.footer-contact{position:absolute;left:920px;top:24px;font-size:11px;line-height:22px}
.footer-contact h3{color:var(--white);font-size:18px;font-weight:600;margin-bottom:8px}
.footer-contact .row{display:flex;align-items:center;gap:8px}
.socials{display:flex;gap:8px;margin-top:12px}
.socials span{width:24px;height:24px;border-radius:50%;background:#3b4145}
.footer-bar{position:absolute;top:2220px;left:0;width:1200px;height:40px;background:var(--footer-bar);color:#8d9397;font-size:11px;line-height:40px;padding-left:28px}
</style>
</head>
<body>

<header class="site-header">
  <div class="brand"><span class="brand-mark"></span>Rosetta Cleans</div>
  <div class="header-contact">321-555-0187<br>info@rosetta-cleans.com</div>
  <nav class="main-nav">
    <a class="active" href="#">Home</a>
    <a href="#">Services</a>
    <a href="#">Contact</a>
    <a href="#">Free Estimate</a>
    <a href="#">About</a>
  </nav>
</header>

<section class="hero">
  <div class="hero-photo" role="img" aria-label="Housekeeper in gloves wiping a kitchen counter in a bright home"></div>
  <div class="hero-badge">
    <div class="hero-badge-inner">
      <div class="name">Rosetta Cleans</div>
      <div class="tag">Maid Services</div>
      <div class="call">Call us today</div>
      <div class="phone">321-555-0187</div>
    </div>
  </div>
  <form class="contact-card">
    <h2>Contact Us</h2>
    <p>Leave your details below and we will call you back the same day.</p>
    <div class="field">Name</div>
    <div class="field">Email</div>
    <div class="field">Phone</div>
    <div class="field">Message</div>
    <div class="btn">Submit</div>
  </form>
</section>

<section class="about">
  <svg class="zigzag" style="top:0" viewBox="0 0 1200 12" preserveAspectRatio="none">
    <pattern id="zz" width="24" height="12" patternUnits="userSpaceOnUse"><path d="M0 0H24L12 12Z" fill="#eef3f5"/></pattern>
    <rect width="1200" height="12" fill="url(#zz)"/></svg>
  <div class="section-title">About Us<div class="title-rule"></div></div>
  <p class="about-text">Rosetta Cleans has been cleaning Seminole County homes for over twelve years. We are trusted by your neighbors, affordable and flexible to fit your schedule, and we back every visit with our 200% money back guarantee. Ask about same day cleanings and up to 20% off continued cleanings for regular clients.</p>
  <div class="btn">Book Now</div>
  <div class="about-photo" role="img" aria-label="Team of five cleaners in uniforms standing with mops and buckets"></div>
  <svg class="zigzag" style="bottom:-12px" viewBox="0 0 1200 12" preserveAspectRatio="none">
    <pattern id="zz2" width="24" height="12" patternUnits="userSpaceOnUse"><path d="M0 0H24L12 12Z" fill="#4fd0bf"/></pattern>
    <rect width="1200" height="12" fill="url(#zz2)"/></svg>
</section>

<section class="services">
  <div class="section-title">Our Services<div class="title-rule"></div></div>

  <div class="service" style="left:130px;top:190px">
    <div class="service-icon"><svg width="26" height="26" viewBox="0 0 24 24" fill="none" stroke="#fff" stroke-width="2"><path d="M3 11l9-7 9 7v9H3z"/><path d="M10 20v-6h4v6"/></svg></div>
    <div><h3>House Cleaning</h3><p>Kitchens, baths and living rooms cleaned top to bottom on your schedule.</p></div>
  </div>
  <div class="service" style="left:130px;top:300px">
    <div class="service-icon"><svg width="26" height="26" viewBox="0 0 24 24" fill="none" stroke="#fff" stroke-width="2"><rect x="5" y="3" width="14" height="18"/><path d="M9 7h2M13 7h2M9 11h2M13 11h2M9 15h2M13 15h2"/></svg></div>
    <div><h3>Office Cleaning</h3><p>Desks, floors and shared spaces kept fresh for your whole team.</p></div>
  </div>
  <div class="service" style="left:130px;top:410px">
    <div class="service-icon"><svg width="26" height="26" viewBox="0 0 24 24" fill="none" stroke="#fff" stroke-width="2"><circle cx="12" cy="9" r="6"/><path d="M12 15v7"/></svg></div>
    <div><h3>Garden Cleaning</h3><p>Patios, porches and outdoor areas swept and tidied with care.</p></div>
  </div>

  <div class="services-photo" role="img" aria-label="Cleaner holding a mop and a bucket of cleaning supplies"></div>
  <div class="services-base"></div>

  <div class="service" style="left:800px;top:190px">
    <div class="service-icon"><svg width="26" height="26" viewBox="0 0 24 24" fill="none" stroke="#fff" stroke-width="2"><rect x="4" y="4" width="16" height="16"/><path d="M12 4v16M4 12h16"/></svg></div>
    <div><h3>Window Cleaning</h3><p>Streak free glass inside and out, frames and sills included.</p></div>
  </div>
  <div class="service" style="left:800px;top:300px">
    <div class="service-icon"><svg width="26" height="26" viewBox="0 0 24 24" fill="none" stroke="#fff" stroke-width="2"><rect x="3" y="7" width="18" height="10"/><path d="M3 19h18"/></svg></div>
    <div><h3>Carpet Cleaning</h3><p>Deep carpet care that lifts stains and brings back softness.</p></div>
  </div>
  <div class="service" style="left:800px;top:410px">
    <div class="service-icon"><svg width="26" height="26" viewBox="0 0 24 24" fill="none" stroke="#fff" stroke-width="2"><circle cx="12" cy="12" r="9"/><path d="M12 7v5l3 3"/></svg></div>
    <div><h3>24 hr Services</h3><p>Same day and round the clock bookings when you need help fast.</p></div>
  </div>
</section>

<section class="offers">
  <svg class="zigzag" style="top:-12px" viewBox="0 0 1200 12" preserveAspectRatio="none">
    <pattern id="zz3" width="24" height="12" patternUnits="userSpaceOnUse"><path d="M0 12H24L12 0Z" fill="#62d8c8"/></pattern>
    <rect width="1200" height="12" fill="url(#zz3)"/></svg>
  <div class="section-title">What We Offer<div class="title-rule"></div></div>
  <div class="offer" style="left:180px">
    <div class="offer-ring"><div class="offer-disc"><div class="lead">1st Time</div><div class="value">$25<small>off</small></div></div></div>
    <div class="offer-caption">1st deep clean $25 Off</div>
  </div>
  <div class="offer" style="left:480px">
    <div class="offer-ring"><div class="offer-disc"><div class="lead">Bi-Weekly Cleanings</div><div class="value">10%<small>off</small></div></div></div>
    <div class="offer-caption">10% Off Bi-Weekly Cleanings</div>
  </div>
  <div class="offer" style="left:780px">
    <div class="offer-ring"><div class="offer-disc"><div class="lead">Weekly Cleanings</div><div class="value">20%<small>off</small></div></div></div>
    <div class="offer-caption">20% Off Weekly Cleanings</div>
  </div>
</section>

<section class="clients">
  <div class="section-title">Our Clients Are Happy<div class="title-rule"></div></div>
  <svg class="quote-mark" viewBox="0 0 36 36"><circle cx="18" cy="18" r="18" fill="#4fd0bf"/><path d="M11 21c0-4 2-6 5-7v2c-2 1-2 2-2 3h2v4h-5zM19 21c0-4 2-6 5-7v2c-2 1-2 2-2 3h2v4h-5z" fill="#fff"/></svg>
  <p class="quote-text">"Rosetta has been cleaning my home for the past 3 1/2 years and I couldn't be happier with her. I trust her with cleaning my home while I'm out of town and recommend her to my friends."</p>
  <div class="dots"><span class="on"></span><span></span><span></span></div>
</section>

<section class="newsletter">
  <h2>Newsletter Signup</h2>
  <div class="field">Enter your email</div>
  <div class="btn">Signup</div>
</section>

<footer class="site-footer">
  <ul class="footer-col" style="left:100px"><li>About Us</li><li>Our Team</li><li>Cleaning Checklist</li><li>Client Stories</li></ul>
  <ul class="footer-col" style="left:360px"><li>Become a Cleaning Partner</li><li>Service Areas Nearby</li><li>Pricing Details Online</li><li>Book a Cleaning in 30 Seconds</li></ul>
  <ul class="footer-col" style="left:640px"><li>How We Keep Homes Fresh</li><li>Free Estimate</li><li>Contact</li></ul>
  <div class="footer-contact">
    <h3>Contact</h3>
    <div class="row"><svg width="12" height="12" viewBox="0 0 24 24" fill="none" stroke="#4fd0bf" stroke-width="2"><rect x="2" y="5" width="20" height="14"/><path d="M2 5l10 8 10-8"/></svg>info@rosetta-cleans.com</div>
    <div class="row"><svg width="12" height="12" viewBox="0 0 24 24" fill="#4fd0bf"><path d="M6 2l4 4-2 3c1 3 3 5 6 6l3-2 4 4-3 4C9 21 3 15 2 5z"/></svg>321-555-0187</div>
    <div class="socials"><span></span><span></span><span></span><span></span><span></span></div>
  </div>
</footer>
<div class="footer-bar">© 2017. All rights reserved Rosetta Cleans.com</div>

</body>
</html>
```